Wine business webpage
Italian fine wines
Project: Wine business webpage
Wine business webpage -
Creative Brief
Fine and Rare Italian wine merchant
Cantina del Sole specializes in the Italy's fine and rare wines. We have special relationships with many of the greatest estates and their distributors, and are able to pass on the benefits of those relationships to our customers. We would welcome the opportunity to put our passion and knowledge to work for you!
Dislike: homepage with loads of bottles of wine, e.g. http://www.vintageharborcellars.example/
Nature
natural wood
green - Terre Verte
earth tone
top
http://www.marlowecask.example/
http://www.grapeledgerhub.example/
http://www.vinoquay.example/

```html
<!DOCTYPE html>
<html lang="en">
<head>
<meta charset="utf-8">
<title>Cantina del Sole – Fine and Rare Italian Wines</title>
<link rel="stylesheet" href="https://fonts.googleapis.com/css2?family=Libre+Baskerville:wght@400;700&family=Arimo:wght@400;700&display=swap">
<style>
  :root {
    --bg-wood: #3b2217;
    --bg-wood-dark: #24140d;
    --bg-footer: #1c100a;
    --panel: #ffffff;
    --frame: #e9e2cf;
    --nav-red: #5a1a14;
    --nav-red-dark: #3e100c;
    --olive: #6b6a1e;
    --olive-dark: #4d4c12;
    --bar-brown: #2e1a10;
    --wine: #8a1a1a;
    --text: #333333;
    --muted: #777777;
    --gold: #e8c774;
    --cream: #f4efe1;
  }
  * { box-sizing: border-box; margin: 0; padding: 0; }
  html, body { width: 1200px; height: 1021px; overflow: hidden; }
  body {
    position: relative;
    font-family: "Arimo", Arial, sans-serif;
    color: var(--text);
    background:
      linear-gradient(180deg, rgba(0,0,0,0) 0, rgba(0,0,0,0) 860px, var(--bg-footer) 880px, var(--bg-footer) 100%),
      radial-gradient(ellipse at 50% 30%, #4e2d1d 0%, var(--bg-wood) 45%, var(--bg-wood-dark) 100%);
  }
  .brand {
    position: absolute; left: 200px; top: 70px; width: 230px;
    display: flex; align-items: center; gap: 12px;
  }
  .brand-mark { width: 22px; height: 22px; background: var(--cream); flex: none; }
  .brand-name {
    font-family: "Libre Baskerville", Georgia, serif; font-weight: 400;
    font-size: 30px; line-height: 1.15; color: var(--cream);
  }
  .cart {
    position: absolute; left: 912px; top: 33px; width: 180px; height: 55px;
    background: rgba(20,10,6,0.75); border-radius: 3px;
    display: flex; align-items: center; justify-content: center; gap: 12px;
    font-family: "Libre Baskerville", Georgia, serif; font-size: 15px; color: #fff;
  }
  .main-nav {
    position: absolute; left: 434px; top: 140px; width: 658px; height: 76px;
    background: linear-gradient(180deg, var(--nav-red) 0%, var(--nav-red-dark) 100%);
    border: 4px solid #fff; border-bottom: 0;
    display: flex; align-items: center; justify-content: space-around; padding: 0 20px;
  }
  .main-nav a {
    font-family: "Libre Baskerville", Georgia, serif; font-size: 14px;
    color: #fff; text-decoration: none; letter-spacing: 0.5px;
  }
  .content {
    position: absolute; left: 434px; top: 216px; width: 658px; height: 663px;
    background: var(--panel); border: 4px solid #fff;
  }
  .hero {
    position: absolute; left: 4px; top: 7px; width: 642px; height: 266px;
    background: linear-gradient(120deg, #f3efe8 0%, #c9b79d 35%, #2a1d19 60%, #6b5648 80%, #d9ccb7 100%);
  }
  .welcome {
    position: absolute; left: 18px; top: 300px;
    font-family: "Libre Baskerville", Georgia, serif; font-size: 17px; color: #2a1a10;
  }
  .intro {
    position: absolute; left: 18px; top: 334px; width: 610px;
    font-size: 12px; line-height: 17px; color: #444;
  }
  .column { position: absolute; top: 440px; width: 290px; }
  .column.arrivals { left: 17px; }
  .column.pick { left: 354px; }
  .column h2 {
    background: var(--bar-brown); color: #fff; height: 24px;
    font-size: 13px; font-weight: 700; letter-spacing: 1px;
    padding: 5px 12px; text-transform: uppercase;
  }
  .column p { margin: 18px 10px 0; font-size: 12px; line-height: 17px; color: #444; }
  .column ul { list-style: none; margin: 14px 10px 0; }
  .column li { font-size: 12px; line-height: 23px; color: var(--wine); text-decoration: underline; }
  .column li:first-child { border-top: 1px solid #ddd; padding-top: 4px; }
  .sidebar {
    position: absolute; left: 111px; top: 218px; width: 310px; height: 630px;
    background: var(--frame); padding: 6px;
  }
  .search {
    height: 100px; background: linear-gradient(90deg, var(--olive-dark), var(--olive));
    position: relative; padding: 10px 14px;
  }
  .search h3 {
    font-family: "Libre Baskerville", Georgia, serif; font-size: 18px; color: #fff; font-weight: 700;
  }
  .search-field {
    margin-top: 10px; display: flex; gap: 4px; align-items: center;
  }
  .search-field span { display: block; width: 140px; height: 22px; background: #fff; border: 1px solid #999; }
  .search-field b { width: 24px; height: 22px; background: var(--wine); display: flex; align-items: center; justify-content: center; }
  .search .corks {
    position: absolute; right: 8px; top: 10px; width: 110px; height: 80px;
    background: radial-gradient(ellipse at 50% 50%, #d8c092 0%, #a4824e 60%, rgba(107,106,30,0) 100%);
  }
  .box { background: #fff; margin-top: 8px; padding: 12px 20px; }
  .categories { height: 258px; }
  .categories h3 {
    font-family: "Libre Baskerville", Georgia, serif; font-size: 19px; color: var(--wine); font-weight: 700;
  }
  .categories ul { margin: 10px 0 0 24px; }
  .categories li { font-size: 12px; line-height: 19px; color: #222; }
  .inventory { height: 118px; display: flex; gap: 16px; padding: 10px 14px; }
  .inventory-photo { width: 112px; height: 98px; flex: none; background: radial-gradient(circle at 40% 50%, #c9301f 0%, #6e1510 50%, #e8e2da 100%); }
  .inventory h3 { font-size: 16px; font-weight: 700; color: #222; letter-spacing: 1px; line-height: 20px; margin-top: 4px; }
  .inventory .formats { list-style: none; margin-top: 8px; }
  .inventory .formats li { font-size: 11px; color: #999; line-height: 16px; display: flex; align-items: center; gap: 6px; }
  .inventory .formats i { width: 9px; height: 9px; border-radius: 50%; border: 1px solid #aaa; display: inline-block; }
  .newsletter { height: 116px; padding: 12px 18px; }
  .newsletter h3 { font-size: 16px; font-weight: 700; color: var(--wine); letter-spacing: 1px; }
  .newsletter p { font-size: 10px; color: #999; line-height: 13px; margin-top: 6px; width: 220px; }
  .signup { display: flex; gap: 6px; margin-top: 10px; }
  .signup span { width: 175px; height: 22px; border: 1px solid #999; font-size: 11px; padding: 3px 6px; color: #333; }
  .signup b { background: var(--wine); color: #fff; font-size: 11px; padding: 4px 8px; }
  .site-footer { position: absolute; left: 0; top: 890px; width: 1200px; text-align: center; }
  .footer-nav a { font-size: 13px; color: var(--gold); text-decoration: none; }
  .footer-nav span { color: var(--gold); margin: 0 6px; font-size: 13px; }
  .copyright { margin-top: 10px; font-size: 11px; color: #ddd; }
</style>
</head>
<body>
  <header>
    <div class="brand">
      <span class="brand-mark"></span>
      <span class="brand-name">Cantina del Sole</span>
    </div>
    <div class="cart">
      Shopping Cart
      <svg width="24" height="20" viewBox="0 0 24 20" aria-hidden="true">
        <path d="M1 2h4l3 11h12l3-8H7" fill="none" stroke="#fff" stroke-width="2"/>
        <circle cx="10" cy="17" r="2" fill="#fff"/><circle cx="18" cy="17" r="2" fill="#fff"/>
      </svg>
    </div>
    <nav class="main-nav">
      <a href="#">HOME</a><a href="#">ABOUT US</a><a href="#">OUR WINES</a>
      <a href="#">ORDERING</a><a href="#">NEWS</a><a href="#">CONTACT US</a>
    </nav>
  </header>

  <aside class="sidebar">
    <div class="search">
      <h3>Search for Wine</h3>
      <div class="search-field">
        <span></span>
        <b><svg width="12" height="12" viewBox="0 0 12 12" aria-hidden="true"><circle cx="5" cy="5" r="3.5" fill="none" stroke="#fff" stroke-width="1.5"/><path d="M8 8l3 3" stroke="#fff" stroke-width="1.5"/></svg></b>
      </div>
      <div class="corks" role="img" aria-label="Wine corks"></div>
    </div>
    <div class="box categories">
      <h3>Categories</h3>
      <ul>
        <li>Australian</li><li>Bordeaux</li><li>Burgundy</li><li>Cabernet</li>
        <li>Champagne</li><li>Chardonnay</li><li>Italian</li><li>Merlot</li>
        <li>Other</li><li>Port</li><li>Rhone</li>
      </ul>
    </div>
    <div class="box inventory">
      <div class="inventory-photo" role="img" aria-label="Red wine being poured into a glass"></div>
      <div>
        <h3>DOWNLOAD<br>INVENTORY</h3>
        <ul class="formats"><li><i></i>PDF</li><li><i></i>Excel</li></ul>
      </div>
    </div>
    <div class="box newsletter">
      <h3>CANTINA NEWSLETTER</h3>
      <p>Learn what's new at Cantina by joining our newsletter</p>
      <div class="signup"><span>Your email address</span><b>SEND</b></div>
    </div>
  </aside>

  <main class="content">
    <div class="hero" role="img" aria-label="Wine bottles resting in a wooden crate"></div>
    <h1 class="welcome">Welcome to Cantina del Sole</h1>
    <p class="intro">Lorem ipsum dolor sit amet, consectetur adipisicing elit, sed do eiusmod tempor incididunt ut labore et dolore magna aliqua. Ut enim ad minim veniam, quis nostrud exercitation ullamco laboris nisi ut aliquip ex ea commodo consequat. Duis aute irure dolor in reprehenderit in voluptate velit esse cillum dolore eu fugiat nulla pariatur. Excepteur sint occaecat cupidatat non proident, sunt in culpa qui officia deserunt mollit anim id est laborum.</p>
    <section class="column arrivals">
      <h2>New Arrivals</h2>
      <p>Lorem ipsum dolor sit amet, consectetur adipisicing elit, sed do eiusmod tempor incididunt ut labore et</p>
      <ul><li>Lorem ipsum dolor sit amet,</li><li>consectetur adipisicing elit, sed do</li><li>eiusmod tempor incididunt ut labore et</li></ul>
    </section>
    <section class="column pick">
      <h2>Pick of the Month</h2>
      <p>Lorem ipsum dolor sit amet, consectetur adipisicing elit, sed do eiusmod tempor incididunt ut labore et</p>
      <ul><li>Lorem ipsum dolor sit amet,</li><li>consectetur adipisicing elit, sed do</li><li>eiusmod tempor incididunt ut labore et</li></ul>
    </section>
  </main>

  <footer class="site-footer">
    <nav class="footer-nav">
      <a href="#">Home</a><span>|</span><a href="#">About Us</a><span>|</span><a href="#">Our wines</a><span>|</span><a href="#">Ordering</a><span>|</span><a href="#">News</a><span>|</span><a href="#">Contact Us</a>
    </nav>
    <p class="copyright">© 2011 Cantina del Sole</p>
  </footer>
</body>
</html>
```